Business Card Design Project

I am a property development company requiring a professional looking business card.
The name of the my company is KLV SUMMITRA. I have attached a couple of designs that I have created on my own, that can give you an idea of what I am after.
Above the wording KLV SUMMITRA, I have a orange arc above these words to signify the sun is begining to rise above the horizon.
I have a few designs; Middle Rays, Side Rays, Horizontals Rays which are OK, but I am looking for the better design.
The Rear design of the card is what I had came up with. If you have a better design, I am happy to see it.
The design of the card can follow what I have came up with, or it can be totally different. The fonts needs to be adjusted to another font that is more suitable.
The colours that I have used is what I think I would like to stick with. As I have mentioned, the orange arc is to signify the sun rising. If you have a better colour scheme, I would consider it.
Looking at dealing with first home buyers and proffesional people.
Business

```html
<!DOCTYPE html>
<html lang="en">
<head>
<meta charset="utf-8">
<title>KLV SUMMITRA – Business Card</title>
<link href="https://fonts.googleapis.com/css2?family=Arimo:wght@400;700&family=Open+Sans:ital,wght@1,700&display=swap" rel="stylesheet">
<style>
  :root {
    --page: #ece8e4;
    --orange: #f26a1b;
    --orange-light: #f7923a;
    --red: #e8262a;
    --white: #ffffff;
    --ink: #1e1e1e;
    --tagline: #fff3d6;
  }
  * { margin: 0; padding: 0; box-sizing: border-box; }
  html, body { width: 1200px; height: 900px; overflow: hidden; }
  body {
    background: var(--page);
    font-family: "Arimo", Arial, sans-serif;
    position: relative;
  }
  .card {
    position: absolute;
    top: 282px;
    width: 540px;
    height: 336px;
    overflow: hidden;
    box-shadow: 0 4px 14px rgba(0,0,0,0.18);
  }
  .card--front { left: 40px; }
  .card--back { left: 620px; }
  .card__art { position: absolute; inset: 0; }
  .card__content {
    position: absolute;
    inset: 0;
    text-align: center;
  }
  .brand-name {
    position: absolute;
    left: 0; right: 0;
    top: 140px;
    font-size: 36px;
    font-weight: 400;
    letter-spacing: 1px;
    line-height: 1;
  }
  .brand-descriptor {
    position: absolute;
    left: 0; right: 0;
    top: 182px;
    font-size: 16px;
    line-height: 1;
  }
  .card--front .brand-name,
  .card--front .brand-descriptor { color: var(--ink); }
  .card--back .brand-name,
  .card--back .brand-descriptor { color: var(--white); }
  .contact-name {
    position: absolute;
    left: 0; right: 0;
    top: 215px;
    font-size: 16px;
    color: var(--ink);
  }
  .contact-name strong { color: var(--orange); font-weight: 700; }
  .contact-details {
    position: absolute;
    left: 0; right: 0;
    top: 252px;
    font-size: 14px;
    line-height: 17px;
    color: var(--ink);
  }
  .contact-details b { font-weight: 700; }
  .tagline {
    position: absolute;
    left: 0; right: 0;
    top: 212px;
    font-family: "Open Sans", Arial, sans-serif;
    font-style: italic;
    font-weight: 700;
    font-size: 22px;
    color: var(--tagline);
  }
  .web-address {
    position: absolute;
    left: 0; right: 0;
    top: 284px;
    font-size: 14px;
    letter-spacing: 3px;
    color: var(--white);
  }
</style>
</head>
<body>
  <section class="card card--front">
    <svg class="card__art" width="540" height="336" viewBox="0 0 540 336">
      <defs>
        <radialGradient id="front-glow" cx="50%" cy="100%" r="80%">
          <stop offset="0%" stop-color="#f79a45"/>
          <stop offset="100%" stop-color="#f06418"/>
        </radialGradient>
      </defs>
      <rect width="540" height="336" fill="url(#front-glow)" role="img" aria-label="Orange sunburst rays radiating from behind the horizon"/>
      <path d="M0,130 Q270,30 540,130 L540,336 L0,336 Z" fill="var(--white)"/>
    </svg>
    <div class="card__content">
      <h1 class="brand-name">KLV SUMMITRA</h1>
      <p class="brand-descriptor">Property Developments</p>
      <p class="contact-name"><strong>Marcus Reid</strong> - Director</p>
      <p class="contact-details">
        27 Harbour Lane Kirrawee NSW 2232 Australia<br>
        <b>Phone</b> 0412 358 904<br>
        marcus@klvsummitra.com.au<br>
        www.klvsummitra.com.au
      </p>
    </div>
  </section>

  <section class="card card--back">
    <svg class="card__art" width="540" height="336" viewBox="0 0 540 336">
      <defs>
        <linearGradient id="back-fill" x1="0" y1="0" x2="0" y2="1">
          <stop offset="0%" stop-color="#f47a22"/>
          <stop offset="35%" stop-color="#ea2d28"/>
          <stop offset="100%" stop-color="#f26a1b"/>
        </linearGradient>
        <radialGradient id="back-rays" cx="50%" cy="45%" r="60%">
          <stop offset="0%" stop-color="#f7923a" stop-opacity="0"/>
          <stop offset="100%" stop-color="#f7923a" stop-opacity="0.55"/>
        </radialGradient>
      </defs>
      <rect width="540" height="336" fill="url(#back-fill)"/>
      <rect width="540" height="120" fill="url(#back-rays)" role="img" aria-label="Soft orange sunburst rays along the top edge"/>
    </svg>
    <div class="card__content">
      <h2 class="brand-name">KLV SUMMITRA</h2>
      <p class="brand-descriptor">Property Developments</p>
      <p class="tagline">Building upon our Honesty &amp; Integrity</p>
      <p class="web-address">www.klvsummitra.com.au</p>
    </div>
  </section>
</body>
</html>
```